Building Company Business Card Design

I am looking to get a business card designed for my Building Company. Please find the logo attached.

Industry/Entity Type

Business

Contact Information for Business Card

Mobile 0472 913 046
Email admin@tarrowconstructworks.com.au
Website www.tarrowconstructworks.com.au

Colors
0255a3

```html
<!DOCTYPE html>
<html lang="en">
<head>
<meta charset="utf-8">
<title>Tarrow Construct Works – Business Card</title>
<link href="https://fonts.googleapis.com/css2?family=Michroma&family=Montserrat:wght@300;600&display=swap" rel="stylesheet">
<style>
  :root {
    --brand-blue: #1557a3;
    --stripe-grey: #77787b;
    --paper: #f7f7f6;
    --backdrop: #e4e4e4;
    --ink-white: #ffffff;
  }
  * { margin: 0; padding: 0; box-sizing: border-box; }
  html, body {
    width: 1200px; height: 1000px; overflow: hidden;
    background: var(--backdrop);
  }
  .stage { position: relative; width: 1200px; height: 1000px; }

  .card {
    position: absolute;
    width: 700px; height: 400px;
    background: var(--paper);
    overflow: hidden;
    box-shadow: 0 6px 18px rgba(0,0,0,0.12);
  }
  .card--front { left: 250px; top: 70px; }
  .card--back  { left: 250px; top: 530px; }

  .stripe { position: absolute; left: 0; width: 100%; background: var(--stripe-grey); height: 9px; }
  .band   { position: absolute; left: 0; width: 100%; background: var(--brand-blue); }

  /* front */
  .card--front .stripe--top    { top: 172px; }
  .card--front .band           { top: 185px; height: 172px; }
  .card--front .stripe--bottom { top: 361px; }

  .wordmark {
    position: absolute; left: 0; width: 100%;
    text-align: center;
    font-family: "Montserrat", sans-serif;
    font-weight: 600;
    letter-spacing: 0.04em;
    text-transform: uppercase;
  }
  .card--front .wordmark { top: 78px; font-size: 22px; color: var(--brand-blue); }

  .holder {
    position: absolute; left: 70px; top: 243px;
    font-family: "Michroma", sans-serif;
    color: var(--ink-white);
    font-size: 17px; line-height: 1.25;
    letter-spacing: 0.06em;
    text-transform: uppercase;
  }
  .holder .title { padding-left: 88px; }

  .contact {
    position: absolute; left: 380px; top: 205px;
    font-family: "Montserrat", sans-serif;
    font-weight: 300;
    color: var(--ink-white);
    font-size: 10.5px; line-height: 1.55;
    list-style: none;
  }

  /* back */
  .card--back .stripe--top    { top: 14px; }
  .card--back .band           { top: 27px; height: 334px; }
  .card--back .stripe--bottom { top: 365px; }
  .card--back .wordmark { top: 182px; font-size: 28px; color: var(--ink-white); }
</style>
</head>
<body>
<main class="stage">

  <section class="card card--front" aria-label="Business card front">
    <p class="wordmark">Tarrow Construct Works</p>
    <div class="stripe stripe--top"></div>
    <div class="band"></div>
    <div class="stripe stripe--bottom"></div>
    <div class="holder">
      <p class="name">Name Surname</p>
      <p class="title">Title</p>
    </div>
    <ul class="contact">
      <li>Address: PO Box 4172 Elmsbury NSW 2041 AUD</li>
      <li>Telephone: 0472 913 046</li>
      <li>E-posta: admin@tarrowconstructworks.com.au</li>
      <li>Web sitesi: www.tarrowconstructworks.com.au</li>
    </ul>
  </section>

  <section class="card card--back" aria-label="Business card back">
    <div class="stripe stripe--top"></div>
    <div class="band"></div>
    <div class="stripe stripe--bottom"></div>
    <p class="wordmark">Tarrow Construct Works</p>
  </section>

</main>
</body>
</html>
```